Business card design needed

we do security the old cards we have are very out of date
i would love something with a fox and fire that pops
as you could tell on the description we do cctv and alarms so if you could add that some how it would be perfect
thank you very much
Industry/Entity Type
Security
Contact Information for Business Card
Wrenlock industries Pty Ltd
Intruder alarms / access contol. cctv sales . service , installation repairs & 24 hour monitoring
Colin Marsh - technician
ph: 07 38516204
fax: 07 38516294
mob: 0418732945
email: colinm@bluvanta.com.au
ABN: 46 219 807 352

```html
<!DOCTYPE html>
<html lang="en">
<head>
<meta charset="utf-8">
<title>Wrenlock Industries – Business Card</title>
<link rel="stylesheet" href="https://fonts.googleapis.com/css2?family=PT+Sans:wght@400;700&display=swap">
<style>
  :root {
    --page-bg: #e9e9ec;
    --navy: #1d2a8c;
    --blue-deep: #1a2a96;
    --blue-mid: #2c4fc0;
    --blue-light: #3c9be0;
    --orange: #e8701c;
    --white: #ffffff;
    --card-light: #f4f4f6;
    --card-grey: #d9dadd;
    --ink: #111111;
  }
  * { box-sizing: border-box; margin: 0; padding: 0; }
  html, body {
    width: 1200px; height: 900px; overflow: hidden;
    background: var(--page-bg);
    font-family: "PT Sans", "Myriad Pro", Arial, sans-serif;
  }
  .canvas {
    width: 1200px; height: 900px;
    display: flex; align-items: center; justify-content: center; gap: 40px;
  }
  .card {
    width: 540px; height: 330px; border-radius: 22px;
    position: relative; overflow: hidden;
    box-shadow: 0 10px 28px rgba(0,0,0,.18);
  }

  /* Back: contact side */
  .card--contact {
    background: linear-gradient(135deg, var(--card-grey) 0%, var(--card-light) 45%, var(--white) 70%, var(--card-grey) 100%);
  }
  .contact-brand {
    position: absolute; left: 44px; top: 70px;
    display: flex; align-items: center; gap: 14px;
  }
  .brand-dot { width: 22px; height: 22px; border-radius: 50%; background: var(--orange); }
  .contact-brand .brand-name {
    font-size: 50px; font-weight: 700; color: var(--navy); letter-spacing: -0.5px; line-height: 1;
  }
  .person {
    position: absolute; right: 30px; top: 170px; text-align: right; color: var(--ink);
  }
  .person-name { font-size: 20px; font-weight: 700; }
  .person-role { font-size: 14px; font-weight: 400; }
  .person-email { font-size: 14px; margin-top: 4px; }
  .contact-band {
    position: absolute; left: 0; right: 0; bottom: 0; height: 98px;
    background: linear-gradient(90deg, var(--blue-deep) 0%, var(--blue-mid) 60%, var(--blue-light) 100%);
    color: var(--white); padding: 24px 30px 0;
    font-size: 15px; line-height: 1.45;
  }
  .contact-band b { font-weight: 700; }

  /* Front: company side */
  .card--company {
    background: linear-gradient(120deg, var(--blue-deep) 0%, var(--blue-mid) 65%, var(--blue-light) 100%);
    color: var(--white); text-align: center;
    display: flex; flex-direction: column; align-items: center; justify-content: center;
    padding: 0 40px;
  }
  .company-brand {
    display: flex; align-items: center; gap: 14px; margin-bottom: 26px;
  }
  .company-brand .brand-name {
    font-size: 54px; font-weight: 700; color: var(--white); letter-spacing: -0.5px; line-height: 1;
  }
  .company-name { font-size: 17px; font-weight: 700; margin-bottom: 4px; }
  .company-services { font-size: 16px; line-height: 1.3; }
  .company-web { font-size: 18px; margin-top: 20px; }
</style>
</head>
<body>
<main class="canvas">
  <section class="card card--contact" aria-label="Business card, contact side">
    <div class="contact-brand">
      <span class="brand-dot"></span>
      <span class="brand-name">Wrenlock</span>
    </div>
    <div class="person">
      <p><span class="person-name">Colin Marsh</span> <span class="person-role">| Technician</span></p>
      <p class="person-email">colinm@bluvanta.com.au</p>
    </div>
    <div class="contact-band">
      <p><b>P:</b> 07 38516204 | <b>F:</b> 07 38516294 | <b>M:</b> 0418732945</p>
      <p>ABN: 46 219 807 352</p>
    </div>
  </section>

  <section class="card card--company" aria-label="Business card, company side">
    <div class="company-brand">
      <span class="brand-dot"></span>
      <span class="brand-name">Wrenlock</span>
    </div>
    <p class="company-name">Wrenlock Industries Pty Ltd</p>
    <p class="company-services">Intruder alarms / access contol. cctv sales . service ,<br>installation repairs &amp; 24 hour monitoring</p>
    <p class="company-web">www.wrenlock.com</p>
  </section>
</main>
</body>
</html>
```